Home care agency

Current website QRVCAREPLUS.com. Need to update and reformat to different pages. use my info from my current website

Target Market(s)

adult children

Industry/Entity Type

Home Health

Coding

Coded - Design and coding required

Number of Pages Required

4 page

Font styles to use
Sans Serif

Colors
3276b5
33a6d7
3277b5
85cae6
85acd3

```html
<!DOCTYPE html>
<html lang="en">
<head>
<meta charset="utf-8">
<title>QRV Care Plus – Home Health</title>
<link rel="stylesheet" href="https://fonts.googleapis.com/css2?family=Poppins:wght@300;400;500;600;700&family=Open+Sans:wght@400;600;700&display=swap">
<style>
:root{
  --blue:#1a9ae8;
  --blue-bright:#0b86e3;
  --blue-deep:#1666b4;
  --blue-dark:#0e5aa8;
  --navy:#0d3a6e;
  --sky:#85cae6;
  --soft:#85acd3;
  --ink:#1f2430;
  --text:#5b6270;
  --line:#d6dbe3;
  --field:#f5f7fa;
  --paper:#f4f5f7;
  --white:#ffffff;
}
*{box-sizing:border-box;margin:0;padding:0}
html,body{width:1200px;height:4392px;overflow:hidden}
body{font-family:"Open Sans",Arial,sans-serif;color:var(--text);background:var(--white);position:relative}
.abs{position:absolute}
h1,h2,h3,h4,.btn,.nav a{font-family:"Poppins",Arial,sans-serif}

/* header */
.topbar{position:absolute;top:0;left:0;width:1200px;height:34px;background:var(--white)}
.topbar .contact{position:absolute;right:148px;top:8px;display:flex;gap:26px;font-size:13px;color:var(--ink)}
.topbar .contact span{display:flex;align-items:center;gap:8px}
.navbar{position:absolute;top:34px;left:0;width:1200px;height:50px;background:var(--blue)}
.nav{position:absolute;left:474px;top:0;height:50px;display:flex;align-items:center;gap:37px}
.nav a{color:var(--white);font-size:12px;font-weight:500;text-decoration:none;letter-spacing:.4px}
.nav-cta{position:absolute;left:929px;top:10px;width:119px;height:31px;border:1px solid rgba(255,255,255,.8);border-radius:4px;color:var(--white);font-size:12px;display:flex;align-items:center;justify-content:center;font-family:"Poppins",sans-serif}
.brand{position:absolute;left:140px;top:4px;width:116px;height:116px;border-radius:50%;background:var(--white);border:4px solid #dfeaf5;display:flex;align-items:center;justify-content:center;flex-direction:column;z-index:3;box-shadow:0 2px 6px rgba(0,0,0,.12)}
.brand b{font-family:"Poppins",sans-serif;font-weight:500;font-size:20px;color:var(--soft);letter-spacing:1px}
.brand small{font-family:"Poppins",sans-serif;font-weight:500;font-size:9px;color:var(--soft);letter-spacing:.5px}

/* hero */
.hero{position:absolute;top:84px;left:0;width:1200px;height:477px;overflow:hidden}
.hero-photo{position:absolute;inset:0;background:linear-gradient(90deg,#dfe3e8 0%,#f1f3f5 35%,#d9dde2 70%,#b9c2cc 100%)}
.hero-ring{position:absolute;left:147px;top:64px;width:344px;height:344px;border-radius:50%;border:2px solid rgba(255,255,255,.85)}
.hero-circle{position:absolute;left:162px;top:79px;width:314px;height:314px;border-radius:50%;background:linear-gradient(200deg,#33a6d7 0%,#1689e6 60%,#1277d8 100%);text-align:center;color:var(--white);padding-top:64px}
.hero-circle .kicker{font-family:"Poppins",sans-serif;font-weight:300;font-size:27px;letter-spacing:3px}
.hero-circle h1{font-size:27px;font-weight:700;line-height:30px;margin-top:2px}
.hero-circle p{font-size:12.5px;line-height:20px;width:250px;margin:12px auto 0}
.hero-circle .btn{display:inline-block;margin-top:16px;border:1px solid var(--white);border-radius:4px;padding:6px 13px;font-size:13px;font-weight:600;letter-spacing:1px}
.dots{position:absolute;left:475px;top:442px;display:flex;gap:10px}
.dots i{width:15px;height:15px;border-radius:50%;background:rgba(255,255,255,.85);display:block}
.dots i:first-child{background:var(--blue)}

/* about */
.about{position:absolute;top:561px;left:0;width:1200px;height:480px;background:var(--white);overflow:hidden}
.about-halo{position:absolute;left:196px;top:56px;width:338px;height:338px;border-radius:50%;background:radial-gradient(circle,#ffffff 55%,#d8eef9 80%,#ffffff 100%)}
.about-photo{position:absolute;left:210px;top:121px;width:306px;height:306px;border-radius:50%;background:linear-gradient(160deg,#c8ced6,#eef0f3 55%,#a9b3bf)}
.about h2{position:absolute;left:593px;top:68px;font-size:33px;font-weight:500;color:var(--ink)}
.about .copy{position:absolute;left:593px;top:143px;width:440px;font-size:11.3px;line-height:21px;color:var(--text)}
.about .copy p+p{margin-top:10px}
.about .copy a{color:var(--blue-deep);text-decoration:none}
.faint-mark{position:absolute;border-radius:50%;border:10px solid rgba(133,202,230,.18);display:flex;align-items:center;justify-content:center;font-family:"Poppins",sans-serif;font-weight:500;color:rgba(133,172,211,.22)}

/* services */
.services{position:absolute;top:1041px;left:0;width:1200px;height:420px;background:#0b84e0;color:var(--white);overflow:hidden}
.services .texture{position:absolute;left:0;top:0;width:440px;height:420px;background:linear-gradient(120deg,#2a9cf0 0%,#1489e6 50%,#0b84e0 100%)}
.services h2{position:absolute;left:150px;top:98px;font-size:32px;font-weight:600}
.services h3{position:absolute;left:150px;top:152px;font-size:17px;font-weight:500}
.services .why{position:absolute;left:150px;top:186px;width:260px;font-size:11.3px;line-height:21px}
.services .why p+p{margin-top:12px}
.svc-col{position:absolute;top:0}
.svc-icon{position:absolute;top:62px;width:70px;height:70px;border-radius:50%;border:1px solid rgba(255,255,255,.5);background:rgba(255,255,255,.08);display:flex;align-items:center;justify-content:center}
.svc-col h4{position:absolute;top:150px;left:0;white-space:nowrap;font-size:13px;font-weight:600}
.svc-col ul{position:absolute;top:180px;left:0;list-style:none;white-space:nowrap}
.svc-col li,.ticklist li{position:relative;padding-left:19px;font-size:12.5px;line-height:27.8px}
.svc-col li::before,.ticklist li::before{content:"";position:absolute;left:0;top:8px;width:11px;height:11px;border-radius:50%;border-left:2px solid currentColor;border-top:1px solid transparent;border-bottom:1px solid transparent;border-right:1px solid transparent}

/* payment */
.payment{position:absolute;top:1461px;left:0;width:1200px;height:305px;background:var(--white);overflow:hidden}
.pay-illustration{position:absolute;left:293px;top:45px;width:252px;height:258px;border-radius:14px;background:linear-gradient(160deg,#e9f3fc,#cfe6f9 60%,#b7d8f4)}
.payment h2{position:absolute;left:560px;width:400px;text-align:center;top:93px;font-size:27px;font-weight:400;color:var(--ink);letter-spacing:3px}
.rule{position:absolute;height:3px;width:50px;background:var(--blue);border-radius:2px}
.payment p{position:absolute;left:610px;width:300px;text-align:center;top:158px;font-size:11.3px;line-height:21px}
.btn-fill{position:absolute;border-radius:16px;background:var(--blue-bright);color:var(--white);font-size:12.5px;font-weight:600;display:flex;align-items:center;justify-content:center;letter-spacing:.5px;box-shadow:0 4px 10px rgba(11,134,227,.25)}

/* benefit blocks */
.split{position:absolute;left:0;width:1200px;height:293px;overflow:hidden}
.split .panel{position:absolute;top:0;width:600px;height:100%;background:var(--blue-deep);color:var(--white)}
.split .photo{position:absolute;top:0;width:600px;height:100%}
.split h2{position:absolute;font-size:22px;font-weight:600;text-transform:uppercase;white-space:nowrap}
.split .rule{background:var(--white);height:2px;width:45px}
.ticklist{position:absolute;list-style:none;width:370px}
.ticklist li{line-height:17px;margin-bottom:15px}
.ticklist li::before{top:3px}
.notch{position:absolute;width:0;height:0;border-top:16px solid transparent;border-bottom:16px solid transparent}

/* contact */
.contact{position:absolute;top:2349px;left:0;width:1200px;height:516px;background:var(--paper);overflow:hidden}
.contact h2{position:absolute;left:0;width:1200px;text-align:center;top:42px;font-size:31px;font-weight:500;color:var(--ink)}
.contact .intro{position:absolute;left:230px;width:740px;text-align:center;top:110px;font-size:11.3px;line-height:21px}
.c-col{position:absolute;top:184px;width:215px}
.c-icon{width:62px;height:62px;border-radius:50%;border:1px solid #c9d7e6;background:var(--white);display:flex;align-items:center;justify-content:center}
.c-col h4{margin-top:17px;font-size:13px;font-weight:600;color:var(--ink);text-transform:uppercase}
.c-col p{margin-top:8px;font-size:11.3px;line-height:19.5px}
.c-col strong{display:block;color:var(--ink);font-size:13px;line-height:17px;font-weight:600}

/* inquiry */
.inquiry-band{position:absolute;top:2865px;left:0;width:1200px;height:132px;background:linear-gradient(180deg,#1a9ae8,#0b84e0)}
.inquiry-band h2{position:absolute;left:0;width:1200px;text-align:center;top:38px;font-size:33px;font-weight:600;color:var(--white)}
.inquiry-band .rule{left:575px;top:94px;background:var(--white);height:2px}
.inquiry-band .arrow{position:absolute;left:585px;bottom:-16px;border-left:15px solid transparent;border-right:15px solid transparent;border-top:16px solid #0b84e0}
.form-area{position:absolute;top:2997px;left:0;width:1200px;height:1227px;background:linear-gradient(90deg,#eef0f3 0%,#f7f8fa 30%,#fbfbfc 100%);overflow:hidden}
.form-area .bg-photo{position:absolute;left:0;top:280px;width:360px;height:640px;background:radial-gradient(ellipse at 30% 50%,#e3e6ea 0%,rgba(243,244,246,0) 70%)}
.form-area h2{position:absolute;left:0;width:1200px;text-align:center;top:44px;font-size:28px;font-weight:400;color:var(--ink);letter-spacing:1px}
.card{position:absolute;left:150px;top:114px;width:898px;height:1031px;background:var(--white);box-shadow:0 1px 6px rgba(0,0,0,.04)}
.card h3{position:absolute;left:0;width:898px;text-align:center;font-size:20px;font-weight:400;color:var(--ink)}
.label{position:absolute;font-size:12.5px;color:var(--ink)}
.field{position:absolute;height:48px;border:1px solid var(--line);background:var(--field);font-size:12.5px;color:#707784;padding-left:16px;display:flex;align-items:center}
.field.half-l{left:29px;width:416px}
.field.half-r{left:455px;width:416px}
.field.full{left:29px;width:842px}
.field em{font-style:normal;color:var(--blue)}
.field .dates{display:flex;gap:38px;margin-left:80px;font-size:10px;color:#9aa0aa}
.radios{position:absolute;left:0;width:898px;top:260px;display:flex;justify-content:center;gap:14px;font-size:10px;color:#707784}
.radios span{display:flex;align-items:center;gap:5px}
.radios i{width:10px;height:10px;border-radius:50%;border:1px solid #b7bec8;display:block}
.radios i.on{border:3px solid var(--blue)}

/* footer */
.footer{position:absolute;top:4224px;left:0;width:1200px;height:168px;background:var(--navy);color:var(--white);text-align:center}
.footer .credit{position:absolute;left:0;width:1200px;top:38px;font-size:14px;text-decoration:underline}
.socials{position:absolute;left:556px;top:100px;display:flex;gap:13px}
.socials i{width:20px;height:20px;border-radius:50%;background:var(--white);display:block}
.footer .copy{position:absolute;left:0;width:1200px;top:134px;font-size:11px;color:#c9d6e6}
</style>
</head>
<body>

<header>
  <div class="topbar">
    <div class="contact">
      <span><svg width="16" height="12" viewBox="0 0 16 12"><rect x="1" y="1" width="14" height="10" rx="1" fill="none" stroke="#33a6d7" stroke-width="1.4"/><path d="M1 1l7 6 7-6" fill="none" stroke="#33a6d7" stroke-width="1.4"/></svg>hello@qrvcareplus.com</span>
      <span><svg width="16" height="16" viewBox="0 0 24 24"><path d="M6.6 10.8a15.2 15.2 0 006.6 6.6l2.2-2.2a1 1 0 011-.25 11.4 11.4 0 003.6.6 1 1 0 011 1V20a1 1 0 01-1 1A17 17 0 013 4a1 1 0 011-1h3.5a1 1 0 011 1 11.4 11.4 0 00.6 3.6 1 1 0 01-.25 1z" fill="none" stroke="#33a6d7" stroke-width="1.6"/></svg>555-014-2270</span>
    </div>
  </div>
  <div class="navbar">
    <nav class="nav"><a>HOME</a><a>ABOUT US</a><a>SERVICES</a><a>PAYMENT</a><a>CONTACT US</a></nav>
    <div class="nav-cta">Contact Us</div>
  </div>
  <div class="brand"><b>QRV</b><small>CARE PLUS</small></div>
</header>

<section class="hero">
  <div class="hero-photo" role="img" aria-label="Photo of a nurse in scrubs pointing out a window beside an elderly man in a wheelchair"></div>
  <svg class="abs" style="left:0;top:0" width="1200" height="477"><path d="M1200 380 Q1165 470 1070 477 L1200 477 Z" fill="#fff"/></svg>
  <div class="hero-ring"></div>
  <div class="hero-circle">
    <div class="kicker">PROVIDING</div>
    <h1>CARE THROUGHOUT<br>THE SOUTH SHORE</h1>
    <p>There are many variations of passages of Lorem Ipsum available, but the</p>
    <span class="btn">CONTACT US</span>
  </div>
  <div class="dots"><i></i><i></i><i></i><i></i></div>
</section>

<section class="about">
  <div class="faint-mark" style="left:930px;top:-30px;width:300px;height:300px;font-size:58px">QRV</div>
  <div class="about-halo"></div>
  <div class="about-photo" role="img" aria-label="Portrait of the agency's founding nurse in a white coat with a stethoscope"></div>
  <h2>About The Home Health</h2>
  <div class="copy">
    <p>QRV Care Plus Health Services is owned and operated by Dana Whitfield. Dana is a registered nurse and has been in the health care system since 2001. She has specialized in home care, cardiology, trauma and critical care. She invests in future caregivers and has taught for the nursing programs at <a>Harborview University</a>, <a>HIHS</a>, and <a>Bayside College</a>.</p>
    <p>All QRV Care Plus caregivers have extensive background checks and training regarding HIPAA compliance. We individualize the care of our clients in order to provide the best care possible in their home. QRV Care Plus also ensures full access and understanding of client care at all times with a caregiver binder in the client's home at all times. This binder includes information on the client's care plan along and the notes from their caregivers. This will allow all caregivers and the client's family to have an understanding of the care being provided.</p>
  </div>
</section>

<section class="services">
  <div class="texture" role="img" aria-label="Decorative blue textured background"></div>
  <div class="faint-mark" style="left:960px;top:80px;width:230px;height:230px;font-size:42px;color:rgba(255,255,255,.18);border-color:rgba(11,60,140,.35)">QRV</div>
  <h2>Services</h2>
  <h3>Why Choose Home Care?</h3>
  <div class="why">
    <p>Home care is a cost-effective option that allows clients the ability to receive one-on-one care in the comfort of their own home.</p>
    <p>Home care also provides peace of mind to a client's family, near or far, without taking away a client's independence or privacy.</p>
  </div>
  <div class="svc-col" style="left:489px">
    <div class="svc-icon" style="left:1px"><svg width="34" height="34" viewBox="0 0 24 24" fill="none" stroke="#fff" stroke-width="1.3"><path d="M12 11s-4-2.5-4-5a2 2 0 014-.6A2 2 0 0116 6c0 2.5-4 5-4 5z"/><path d="M2 15h4l3 2h5a1.5 1.5 0 000-3h-3M6 19h8l7-5a1.5 1.5 0 00-2-2l-4 2.5"/></svg></div>
    <h4>SKILLED CARE SERVICES</h4>
    <ul>
      <li>Free Initial Nursing Assessment</li>
      <li>Medication Management</li>
      <li>Wound Care</li>
      <li>Wound Care</li>
      <li>Medical Care Assistance</li>
      <li>Transportation to Medical Appointments</li>
      <li>Care Plan Management</li>
    </ul>
  </div>
  <div class="svc-col" style="left:823px">
    <div class="svc-icon" style="left:1px"><svg width="34" height="34" viewBox="0 0 24 24" fill="none" stroke="#fff" stroke-width="1.3"><rect x="8" y="3" width="6" height="16" rx="3" transform="rotate(-40 11 11)"/><path d="M5.5 8.5l7 6"/><path d="M4 4l16 16"/></svg></div>
    <h4>NON-MEDICAL SERVICES</h4>
    <ul>
      <li>Live-In Care</li>
      <li>Respite Care</li>
      <li>Assisting with Daily Living Activities</li>
      <li>Meal Preparations</li>
      <li>Companionship</li>
      <li>Homemaking</li>
    </ul>
  </div>
</section>

<section class="payment">
  <div class="faint-mark" style="left:65px;top:45px;width:205px;height:205px;font-size:36px">QRV</div>
  <div class="pay-illustration" role="img" aria-label="Illustration of a woman holding a large payment card next to a smartphone showing a shopping screen"></div>
  <h2>PAYMENT OPTIONS</h2>
  <div class="rule" style="left:735px;top:141px"></div>
  <p>QRV Care Plus currently accepts check for service payments (with plans for online payments late 2018.)</p>
  <div class="btn-fill" style="left:653px;top:218px;width:215px;height:31px;font-family:Poppins,sans-serif">PAY NOW</div>
</section>

<section class="split" style="top:1766px">
  <div class="panel" style="left:0">
    <h2 style="left:150px;top:43px">Client Benefits</h2>
    <div class="rule" style="left:150px;top:82px"></div>
    <ul class="ticklist" style="left:150px;top:96px">
      <li>Continuity of care with same caregiver for each client on a regular basis.</li>
      <li>Open communication with owner by phone or email.</li>
      <li>Ongoing communications to client's family by phone or email on a weekly basis (if desired.)</li>
      <li>Streamlined payment process.</li>
    </ul>
  </div>
  <div class="photo" style="left:600px;background:linear-gradient(120deg,#8a8f96,#c9ccd0 45%,#6d7278)" role="img" aria-label="Photo of a doctor in a white coat visiting an elderly man seated at home beside a lamp"></div>
  <div class="notch" style="left:600px;top:130px;border-left:16px solid var(--blue-deep)"></div>
</section>

<section class="split" style="top:2059px">
  <div class="photo" style="left:0;background:linear-gradient(110deg,#dfe2e6,#f3f4f5 40%,#c7ccd2)" role="img" aria-label="Photo of a doctor talking with a smiling elderly couple on a sofa"></div>
  <div class="panel" style="left:600px">
    <h2 style="left:116px;top:47px">Care Schedule/Frequency</h2>
    <div class="rule" style="left:116px;top:86px"></div>
    <ul class="ticklist" style="left:116px;top:100px">
      <li>QRV Care Plus non-medical visits require a four hour minimum visit.</li>
      <li>There are no weekly minimum for medical or non-medical visits.</li>
      <li>Clients needing 24-hour care can save up 30% off of services by using a live-in caregiver. (Live-in caregiver requires personal bedroom and bathroom.)</li>
    </ul>
  </div>
  <div class="notch" style="left:584px;top:130px;border-right:16px solid var(--blue-deep)"></div>
</section>

<section class="contact">
  <div class="faint-mark" style="left:920px;top:120px;width:205px;height:205px;font-size:36px">QRV</div>
  <h2>Contact</h2>
  <p class="intro">Thank you for considering QRV Care Plus for your care needs. Information about your medical conditions, care, and financial situation that you provide to us in writing, via email, on the phone (including information left on voice mails) is held in strictest confidence.</p>
  <div class="c-col" style="left:205px">
    <div class="c-icon"><svg width="30" height="30" viewBox="0 0 24 24" fill="none" stroke="#33a6d7" stroke-width="1.3"><rect x="3" y="4" width="12" height="9" rx="1"/><path d="M7 16h4M9 13v3"/><rect x="15" y="9" width="6" height="11" rx="1"/></svg></div>
    <h4>Contact Online</h4>
    <p>To contact us online, please fill out the care inquiry form below and you will be contacted within 24-48 hours.</p>
  </div>
  <div class="c-col" style="left:489px">
    <div class="c-icon"><svg width="28" height="28" viewBox="0 0 24 24"><path d="M6.6 10.8a15.2 15.2 0 006.6 6.6l2.2-2.2a1 1 0 011-.25 11.4 11.4 0 003.6.6 1 1 0 011 1V20a1 1 0 01-1 1A17 17 0 013 4a1 1 0 011-1h3.5a1 1 0 011 1 11.4 11.4 0 00.6 3.6 1 1 0 01-.25 1z" fill="none" stroke="#33a6d7" stroke-width="1.3"/></svg></div>
    <h4>Contact by Phone</h4>
    <p>If you would like to speak with someone over the phone about your care inquiry, you can contact QRV Care Plus<br>Monday-Friday 9:00am-5:00pm at</p>
    <strong style="font-size:14px;margin-top:2px">555-019-3344.</strong>
  </div>
  <div class="c-col" style="left:772px">
    <div class="c-icon"><svg width="28" height="28" viewBox="0 0 24 24" fill="none" stroke="#33a6d7" stroke-width="1.3"><path d="M12 21s-6-6-6-11a6 6 0 0112 0c0 5-6 11-6 11z"/><circle cx="12" cy="10" r="2.2"/><path d="M6 21h12"/></svg></div>
    <h4>Mailing Address</h4>
    <p>Please mail all service payments and employment applications to:</p>
    <strong>QRV Care Plus Health Services</strong>
    <strong>PO Box 410</strong>
    <strong>Easton, MA 02999</strong>
  </div>
  <div class="btn-fill" style="left:460px;top:436px;width:278px;height:33px;background:var(--blue-dark);font-family:Poppins,sans-serif;font-weight:500">EMPLOYMENT APPLICATION</div>
</section>

<section class="inquiry-band">
  <h2>Care Inquiry Form</h2>
  <div class="rule"></div>
  <div class="arrow"></div>
</section>

<section class="form-area">
  <div class="bg-photo" role="img" aria-label="Soft background photo of a hand holding a pen"></div>
  <h2>Youy Details</h2>
  <div class="card">
    <h3 style="top:30px">Contact Information</h3>
    <div class="label" style="left:44px;top:64px">Contact Name</div>
    <div class="field half-l" style="top:92px">First Name<em>*</em></div>
    <div class="field half-r" style="top:92px">Last Name<em>*</em></div>
    <div class="field half-l" style="top:151px">Phone Number<em>*</em></div>
    <div class="field half-r" style="top:151px">Email Address&nbsp;<em>*</em></div>
    <div class="label" style="left:0;width:898px;text-align:center;top:228px">Best Way to Reach You *</div>
    <div class="radios"><span><i class="on"></i>By Phone</span><span><i></i>By Email</span></div>
    <h3 style="top:292px">Contact Information</h3>
    <div class="label" style="left:44px;top:327px">Client Name</div>
    <div class="field half-l" style="top:349px">First Name<em>*</em></div>
    <div class="field half-r" style="top:349px">Last Name<em>*</em></div>
    <div class="field half-l" style="top:409px">Client Birthdate<span class="dates"><span>MM</span><span>DD</span><span>YYYY</span></span></div>
    <div class="label" style="left:46px;top:484px">Address Where Care Will Be Provided</div>
    <div class="field full" style="top:508px">Address 1</div>
    <div class="field full" style="top:567px">Address 2</div>
    <div class="field half-l" style="top:627px">City<em>*</em></div>
    <div class="field half-r" style="top:627px">State/Province<em>*</em></div>
    <div class="field half-l" style="top:687px">Zip/Postal Code<em>*</em></div>
    <div class="field half-r" style="top:687px">Country<em>*</em></div>
    <div class="label" style="left:46px;top:762px">Please use this area to tell us more about the client and/or services that may be of interest to you</div>
    <div class="field full" style="top:784px;height:116px;align-items:flex-start;padding-top:16px">Message</div>
    <div class="btn-fill" style="left:310px;top:949px;width:278px;height:31px;background:var(--blue-dark);font-family:Poppins,sans-serif;font-weight:500;font-size:12px">SUBMIT CAR INQUIRY</div>
  </div>
</section>

<footer class="footer">
  <div class="credit">Site design by Blue Kite Studio.</div>
  <div class="socials" aria-label="Social media links"><i></i><i></i><i></i></div>
  <div class="copy">© 2019 Home Health.All rights Reserved.</div>
</footer>

</body>
</html>
```